Pediatric Dentist Business Card

I need a business card designed for a dentist who works exclusively with children.
We prefer designs that are out of ordiary that is fun and interesting to kids.

there is no logo since this is a dentists office. The name of the doctor is "Tavor Kesh" if you want to get creative with that.

Target Market(s)

Kids

Industry/Entity Type

Business

Contact Information for Business Card

Anythings that is creative

Colors

Designer to choose colors to be used in the design.

```html
<!DOCTYPE html>
<html lang="en">
<head>
<meta charset="utf-8">
<title>Tavor Kesh – Pediatric Dentist Business Card</title>
<link href="https://fonts.googleapis.com/css2?family=Questrial&display=swap" rel="stylesheet">
<style>
  :root {
    --stage: #808080;
    --stage-edge: #3a3a3a;
    --purple: #4400aa;
    --orange: #ff7a1f;
    --white: #ffffff;
    --pink: #f4a3b8;
    --peach: #ffc79a;
    --lavender: #c7a8ec;
    --mint: #a9dcc4;
    --lemon: #f3eaa0;
    --sky: #b9e2ee;
  }
  * { box-sizing: border-box; margin: 0; padding: 0; }
  html, body { width: 1200px; height: 837px; overflow: hidden; }
  body {
    background: var(--stage);
    border: 1px solid var(--stage-edge);
    position: relative;
    font-family: "Questrial", sans-serif;
  }
  .card {
    position: absolute;
    width: 491px;
    height: 280px;
    border-radius: 12px;
    overflow: hidden;
  }
  .card--front-colour { left: 78px; top: 99px; background: var(--white); }
  .card--front-grey { left: 604px; top: 99px; background: #cdcdcd; }
  .card--back { left: 354px; top: 473px; background: var(--purple); }

  .pattern { position: absolute; inset: 0; }
  .card--front-colour .pattern {
    background:
      radial-gradient(circle at 8% 28%, var(--peach) 0 7%, transparent 15%),
      radial-gradient(circle at 30% 12%, var(--pink) 0 5%, transparent 13%),
      radial-gradient(circle at 88% 10%, var(--pink) 0 6%, transparent 14%),
      radial-gradient(circle at 78% 28%, var(--sky) 0 5%, transparent 12%),
      radial-gradient(circle at 18% 82%, var(--lavender) 0 6%, transparent 14%),
      radial-gradient(circle at 62% 78%, var(--peach) 0 7%, transparent 15%),
      radial-gradient(circle at 92% 70%, var(--lemon) 0 6%, transparent 14%),
      radial-gradient(circle at 40% 60%, var(--mint) 0 4%, transparent 11%),
      radial-gradient(circle at 52% 20%, var(--lemon) 0 4%, transparent 11%),
      radial-gradient(ellipse at 40% 50%, #ffe6d2 0%, var(--white) 70%);
  }
  .card--front-grey .pattern {
    background:
      radial-gradient(circle at 8% 28%, var(--peach) 0 7%, transparent 15%),
      radial-gradient(circle at 30% 12%, var(--pink) 0 5%, transparent 13%),
      radial-gradient(circle at 88% 10%, var(--pink) 0 6%, transparent 14%),
      radial-gradient(circle at 78% 28%, var(--sky) 0 5%, transparent 12%),
      radial-gradient(circle at 18% 82%, var(--lavender) 0 6%, transparent 14%),
      radial-gradient(circle at 62% 78%, var(--peach) 0 7%, transparent 15%),
      radial-gradient(circle at 92% 70%, var(--lemon) 0 6%, transparent 14%),
      radial-gradient(circle at 40% 60%, var(--mint) 0 4%, transparent 11%),
      radial-gradient(circle at 52% 20%, var(--lemon) 0 4%, transparent 11%),
      radial-gradient(ellipse at 40% 50%, #e2e2e2 0%, #c8c8c8 75%);
    opacity: 0.85;
  }

  .brand-name {
    position: absolute;
    left: 0; right: 0;
    top: 140px;
    display: flex;
    align-items: center;
    justify-content: center;
    gap: 10px;
    color: var(--purple);
    font-size: 28px;
    letter-spacing: 0.5px;
  }
  .brand-dot {
    width: 18px; height: 18px;
    border-radius: 50%;
    background: var(--orange);
  }

  .name-band {
    position: absolute;
    left: 0; top: 45px;
    width: 236px; height: 39px;
    background: var(--white);
    color: var(--purple);
    font-size: 23px;
    line-height: 39px;
    padding-left: 48px;
    white-space: nowrap;
  }
  .contact-list {
    position: absolute;
    left: 50px; top: 123px;
    list-style: none;
    color: var(--white);
    font-size: 15.5px;
    letter-spacing: 0.3px;
  }
  .contact-list li {
    display: flex;
    align-items: center;
    height: 26.5px;
    white-space: nowrap;
  }
  .contact-list svg { width: 14px; height: 14px; margin-right: 11px; }
  .back-brand {
    position: absolute;
    right: 14px; bottom: 14px;
    color: var(--orange);
    font-size: 18px;
    display: flex;
    align-items: center;
    gap: 7px;
  }
  .back-brand .brand-dot { width: 12px; height: 12px; }
</style>
</head>
<body>
  <section class="card card--front-colour">
    <div class="pattern" role="img" aria-label="Playful scattered pattern of dental illustrations for kids: teeth, toothbrushes, toothpaste tubes, smiling mouths and dental tools in pastel colours"></div>
    <div class="brand-name"><span class="brand-dot"></span>Tavor Kesh</div>
  </section>

  <section class="card card--front-grey">
    <div class="pattern" role="img" aria-label="Playful scattered pattern of dental illustrations on a grey ground: teeth, toothbrushes, toothpaste tubes, smiling mouths and dental tools"></div>
    <div class="brand-name"><span class="brand-dot"></span>Tavor Kesh</div>
  </section>

  <section class="card card--back">
    <div class="name-band">Dr. Tavor Kesh</div>
    <ul class="contact-list">
      <li>
        <svg viewBox="0 0 16 16" aria-hidden="true"><path fill="#fff" d="M2 6c0-2 2.5-3 6-3s6 1 6 3v1h-3V5.5H5V7H2zM4 8h8l1.5 5h-11z"/></svg>
        (555) 014-2087
      </li>
      <li>
        <svg viewBox="0 0 16 16" aria-hidden="true"><rect x="1.5" y="3.5" width="13" height="9" fill="none" stroke="#fff" stroke-width="1.4"/><path d="M1.5 3.5 8 9l6.5-5.5" fill="none" stroke="#fff" stroke-width="1.4"/></svg>
        tavor@kidsmileclinic.com
      </li>
      <li>
        <svg viewBox="0 0 16 16" aria-hidden="true"><g fill="none" stroke="#fff" stroke-width="1.2"><circle cx="8" cy="8" r="6.5"/><ellipse cx="8" cy="8" rx="3" ry="6.5"/><path d="M1.5 8h13M2.5 4.8h11M2.5 11.2h11"/></g></svg>
        www.kidsmileclinic.com
      </li>
    </ul>
    <div class="back-brand"><span class="brand-dot"></span>Tavor Kesh</div>
  </section>
</body>
</html>
```